Commercial/Corporate Law Firm needs Website Design

Hi guys. I've started up a new law firm and would love your help designing an attractive website. I'll need both design and coding, and to make it easy for us to edit as necessary later, I think it should be built off a Wordpress.org structure.
FIRST IMPRESSIONS
It's very important that the first impression of the website really captures our prospective clients' attention and impresses them. Their first three seconds needs to be good.
I imagine the homepage may be short, with a menu bar and a compelling image, and with a tagline overlaid or underneath (eg. "It's about results.")
The image should be related to our practice areas: eg. IPOs, corporate transactions, or commercial negotiations.
I have previously suggested there could be a skyline image of Sydney or Adelaide. However, because we are based in Adelaide, I don't think Sydney is appropriate - and Adelaide is probably too boring to use.
HOMEPAGE
Being a new firm, we don't have many existing testimonials, and I will be the only lawyer to start with. So we need to focus on the nature of the services we will provide and how my experience can help them. We have an existing logo to use, and I would like the website colour scheme not to clash with that logo (dark blue and white).
After the initial image and tagline there should be a brief introduction to each of the main areas of work, eg. "We specialise in three main areas of practice:"
1. Corporate Transactions and Regulation
2. Business Law and Dispute Resolution
3. Migration Assistance
These should each have an appropriate photo and link to a separate page that briefly describes our services in that area.
Below that there should be a message from me with a photo. Finally, at the bottom, there should be a "Contact Us" section which shows a Google image of our address, contact details, and then our logo with colours inverted.
OTHER PAGES
While we will need some other pages, they should all be fairly simple. I think we will need one page to say "About Us", where I will put information about my experience. I think we will then need one page for each of the 3 areas listed above, which just needs an appropriate image and then text to describe the service. Finally, a "Contact Us" page which I imagine will be the same as the bottom of the homepage.
OTHER DETAILS
For now you can use details from my LinkedIn page to fill out any other text as necessary, or the photo.
Because the logo is square, I would prefer the design of the website also to be rectangular.
Looking forward to seeing your work! Thank you.
Good luck,
Marcus
Target Market(s)
Potential clients:
Businesses with legal issues or disputes
Companies wishing to list on the stock market

```html
<!DOCTYPE html>
<html lang="en">
<head>
<meta charset="utf-8">
<title>Westbrook Legal</title>
<link rel="stylesheet" href="https://fonts.googleapis.com/css2?family=Cinzel:wght@400;500&family=Roboto+Slab:wght@300;400&family=Roboto:ital,wght@0,300;0,400;0,500;1,300;1,400&display=swap">
<style>
:root{
  --navy:#1b3a6b;
  --navy-deep:#142e58;
  --navy-mid:#24497f;
  --navy-ink:#0f2a5a;
  --accent:#3d6fb8;
  --accent-soft:#6f93c9;
  --page-bg:#f3f3f3;
  --panel:#f5f5f5;
  --panel-alt:#efefef;
  --line:#b9b9b9;
  --text:#555;
  --text-soft:#888;
  --white:#fff;
}
*{margin:0;padding:0;box-sizing:border-box}
html,body{width:1200px;height:2356px;overflow:hidden}
body{background:var(--page-bg);font-family:"Roboto",Arial,sans-serif;color:var(--text);position:relative}
.page{position:absolute;left:91px;top:49px;width:1021px;height:2262px;background:var(--white);box-shadow:0 0 14px rgba(0,0,0,.12);overflow:hidden}
.abs{position:absolute}

/* top bar */
.topbar{left:0;top:0;width:100%;height:42px;border-bottom:1px solid #e6e6e6;font-size:12px;color:#777;font-family:"Roboto Slab",Georgia,serif}
.topbar .address{left:0;top:13px;padding-left:0}
.topbar .address{left:0}
.topbar .contact{right:50px;top:13px;display:flex;gap:30px;align-items:center}
.topbar .contact b{color:var(--navy-ink);font-weight:400}
.topbar .contact svg{vertical-align:-2px;margin-right:6px}

/* header */
.header{left:0;top:42px;width:100%;height:85px;border-bottom:1px solid #eee}
.brand{left:46px;top:20px;display:flex;align-items:center;gap:14px}
.brand-square{width:52px;height:52px;background:var(--navy)}
.brand-name{font-family:"Cinzel",Georgia,serif;font-size:27px;color:var(--navy);letter-spacing:2px}
.nav{left:442px;top:34px;display:flex;gap:42px;font-family:"Roboto Slab",Georgia,serif;font-size:12.5px;color:#777}
.nav .active{color:var(--navy-ink)}
.social-top{left:868px;top:27px;display:flex;gap:8px}
.social-top span{width:30px;height:30px;border-radius:50%;background:#e4e4e4;display:block}

/* hero */
.hero-photo{left:0;top:127px;width:1021px;height:477px;background:linear-gradient(160deg,#c9cdd4 0%,#e6e7ea 40%,#d3d6db 70%,#eef0f2 100%)}
.hero-box{left:68px;top:292px;width:884px;height:608px;background:rgba(245,245,245,.72)}
.hero-box-lower{left:68px;top:604px;width:884px;height:296px;background:var(--panel)}
.hero-mark{left:470px;top:234px;width:80px;height:80px;background:var(--navy);border:3px solid #fff;outline:1px solid var(--navy)}
.hero-title{left:0;top:338px;width:1021px;text-align:center;font-family:"Cinzel",Georgia,serif;font-size:40px;color:var(--navy-ink);letter-spacing:4px}
.hero-lead{left:0;top:403px;width:1021px;text-align:center;font-family:"Roboto Slab",Georgia,serif;font-size:15px;line-height:25px;color:#555;letter-spacing:.6px}
.btn{display:flex;align-items:center;justify-content:center;font-family:"Roboto Slab",Georgia,serif;font-size:14px;text-transform:uppercase}
.btn-primary{left:355px;top:493px;width:137px;height:35px;background:var(--navy);color:#fff}
.btn-outline{left:515px;top:493px;width:131px;height:35px;border:1px solid #888;color:#333;background:rgba(255,255,255,.5)}
.frame{border-color:#8a8a8a;border-style:solid;border-width:0}

/* services */
.service{top:648px;width:220px}
.service-head{display:flex;align-items:center;gap:10px;font-family:"Roboto Slab",Georgia,serif;font-size:12.5px;line-height:20px;color:var(--navy-ink);letter-spacing:.6px;height:40px}
.service-body{margin-top:20px;font-family:"Roboto Slab",Georgia,serif;font-style:italic;font-size:12px;line-height:20px;color:#888;font-weight:300}
.service-more{margin-top:19px;display:flex;align-items:center;gap:18px;font-family:"Roboto Slab",Georgia,serif;font-style:italic;font-size:12px;color:#888}

/* stats band */
.stats-photo{left:0;top:926px;width:600px;height:327px;background:linear-gradient(180deg,#5d80b6 0%,#3d609a 55%,#5776a8 100%)}
.hours-panel{left:0;top:926px;width:1021px;height:327px}
.stat{top:1071px;width:110px;text-align:center;color:#fff}
.stat-num{font-family:"Roboto",Arial,sans-serif;font-size:37px;font-weight:300;background:rgba(255,255,255,.18);height:44px;line-height:44px}
.stat-label{font-family:"Roboto Slab",Georgia,serif;font-size:18px;margin-top:8px;white-space:nowrap;margin-left:-20px;margin-right:-20px}
.hours{left:606px;top:1010px;color:#fff}
.hours h2{font-family:"Cinzel",Georgia,serif;font-weight:400;font-size:28px;letter-spacing:1px}
.hours p{font-family:"Roboto Slab",Georgia,serif;font-style:italic;font-size:12px;line-height:19px;color:var(--accent-soft);margin-top:10px;width:330px}
.hours dl{margin-top:14px;font-family:"Roboto Slab",Georgia,serif;font-size:14px;line-height:28px}
.hours dt{display:inline;color:var(--accent-soft)}
.hours dd{display:inline;margin-left:4px}

/* principal */
.principal{left:0;top:1253px;width:1021px;height:322px;background:var(--panel-alt)}
.portrait{left:76px;top:1230px;width:210px;height:210px;border-radius:50%;border:5px solid #fff;background:radial-gradient(circle at 50% 40%,#9a9a9a 0%,#5b5b5b 60%,#3a3a3a 100%)}
.principal-name{left:60px;top:1455px;width:242px;text-align:center;font-family:"Roboto Slab",Georgia,serif;font-size:27px;color:var(--navy-ink)}
.principal-role{left:60px;top:1492px;width:242px;text-align:center;font-family:"Roboto Slab",Georgia,serif;font-size:14px;color:var(--accent)}
.principal-text{left:319px;top:1308px;width:630px;font-family:"Roboto Slab",Georgia,serif;font-style:italic;font-weight:300;font-size:14.5px;line-height:26.5px;color:#666}
.principal-text p+p{margin-top:26px}

/* testimonials */
.testi-title{left:0;top:1620px;width:1021px;text-align:center;font-family:"Cinzel",Georgia,serif;font-size:28px;color:var(--navy-ink);letter-spacing:3px}
.testi-sub{left:0;top:1664px;width:1021px;display:flex;justify-content:center;align-items:center;gap:12px;font-family:"Roboto Slab",Georgia,serif;font-size:12px;color:#888}
.testi-sub i{display:block;width:30px;height:1px;background:#aaa}
.testi-name{left:0;top:1715px;width:1021px;text-align:center;font-family:"Roboto Slab",Georgia,serif;font-size:15px;color:var(--navy-ink);letter-spacing:1px}
.testi-quote{left:160px;top:1750px;width:701px;text-align:center;font-family:"Roboto Slab",Georgia,serif;font-size:12.5px;line-height:20px;color:#888;letter-spacing:.6px}
.arrows{left:480px;top:1836px;display:flex;gap:12px}
.arrows span{width:22px;height:22px;border-radius:50%;border:1px solid #555;display:flex;align-items:center;justify-content:center}

/* call to action */
.cta{left:0;top:1903px;width:1021px;height:125px;background:var(--navy-mid)}
.cta h3{left:110px;top:39px;font-family:"Roboto Slab",Georgia,serif;font-style:italic;font-weight:400;font-size:20px;color:#fff}
.cta p{left:110px;top:72px;font-family:"Roboto Slab",Georgia,serif;font-style:italic;font-size:13px;color:var(--accent)}
.cta .btn{left:756px;top:32px;width:154px;height:63px;border:1px solid #fff;color:#fff;font-size:14px}

/* footer */
.footer{left:0;top:2028px;width:1021px;height:193px;background:var(--navy)}
.footer h4{font-family:"Roboto Slab",Georgia,serif;font-weight:400;font-size:17px;color:#fff}
.news-title{left:113px;top:46px}
.news-form{left:113px;top:86px;width:446px;height:34px;border:1px solid #3b5f96;display:flex}
.news-form span{flex:1;font-family:"Roboto Slab",Georgia,serif;font-size:12px;color:var(--accent-soft);line-height:32px;padding-left:24px}
.news-form b{width:99px;background:var(--navy-deep);color:#fff;font-family:"Roboto Slab",Georgia,serif;font-weight:400;font-size:12px;display:flex;align-items:center;justify-content:center}
.footer-nav{left:113px;top:146px;display:flex;gap:23px;font-family:"Roboto Slab",Georgia,serif;font-size:12px;color:#fff}
.footer-divider{left:674px;top:52px;width:1px;height:72px;background:#2f5288}
.follow-title{left:785px;top:46px}
.follow-links{left:786px;top:88px;display:flex;gap:8px}
.follow-links span{width:34px;height:34px;border-radius:50%;border:1.5px solid #fff;display:block}
.copyright{left:0;top:2221px;width:1021px;height:41px;background:var(--navy-deep);text-align:center;line-height:41px;font-family:"Roboto Slab",Georgia,serif;font-size:12px;color:var(--accent)}
</style>
</head>
<body>
<div class="page">

  <div class="abs topbar">
    <span class="abs address" style="left:46px">Level 2, 48 Harbour Street NORTHFIELD SA 5085</span>
    <div class="abs contact">
      <span><svg width="11" height="11" viewBox="0 0 24 24"><path d="M6.6 10.8a15 15 0 0 0 6.6 6.6l2.2-2.2a1 1 0 0 1 1-.25 11.4 11.4 0 0 0 3.6.57 1 1 0 0 1 1 1V20a1 1 0 0 1-1 1A17 17 0 0 1 3 4a1 1 0 0 1 1-1h3.5a1 1 0 0 1 1 1c0 1.25.2 2.45.57 3.6a1 1 0 0 1-.25 1z" fill="#999"/></svg><b>Telephone:</b> 555 010 2020</span>
      <span style="color:#ddd">|</span>
      <span><svg width="11" height="9" viewBox="0 0 24 18"><rect x="1" y="1" width="22" height="16" fill="none" stroke="#999" stroke-width="2"/><path d="M1 1l11 9 11-9" fill="none" stroke="#999" stroke-width="2"/></svg><b>Email:</b> info@westbrooklegal.example</span>
    </div>
  </div>

  <div class="abs header">
    <div class="abs brand"><span class="brand-square"></span><span class="brand-name">Westbrook Legal</span></div>
    <nav class="abs nav"><span class="active">Home</span><span>About Us</span><span>Services</span><span>News</span><span>Contact Us</span></nav>
    <div class="abs social-top"><span></span><span></span><span></span></div>
  </div>

  <div class="abs hero-photo" role="img" aria-label="Business professionals reviewing documents around a meeting table"></div>
  <div class="abs hero-box"></div>
  <div class="abs hero-box-lower"></div>
  <div class="abs hero-mark"></div>

  <div class="abs frame" style="left:93px;top:319px;width:130px;height:171px;border-left-width:1.5px;border-top-width:1.5px"></div>
  <div class="abs frame" style="left:793px;top:319px;width:131px;height:171px;border-right-width:1.5px;border-top-width:1.5px"></div>

  <h1 class="abs hero-title">It's about results</h1>
  <p class="abs hero-lead">Lorem Ipsum is simply dummy text of the printing and typesetting<br>industry. Lorem Ipsum has &nbsp;type specimen book.</p>
  <div class="abs btn btn-primary">Contact Us</div>
  <div class="abs btn btn-outline">About Us</div>

  <div class="abs frame" style="left:93px;top:702px;width:130px;height:171px;border-left-width:1.5px;border-bottom-width:1.5px"></div>
  <div class="abs frame" style="left:793px;top:702px;width:131px;height:171px;border-right-width:1.5px;border-bottom-width:1.5px"></div>

  <section class="abs service" style="left:126px">
    <div class="service-head">
      <svg width="30" height="34" viewBox="0 0 30 34"><circle cx="9" cy="6" r="4" fill="var(--navy)"/><path d="M2 20a7 7 0 0 1 14 0z" fill="var(--navy)"/><circle cx="22" cy="17" r="4" fill="var(--navy)"/><path d="M15 31a7 7 0 0 1 14 0z" fill="var(--navy)"/><circle cx="6" cy="27" r="3" fill="none" stroke="var(--navy)" stroke-width="2"/></svg>
      <span>Corporate Transactions<br>&amp; Regulation</span>
    </div>
    <p class="service-body">It is a long established fact that a reader will be distractedlooking at its layout. It is a long established fact that a reader will be distracted-looking at its layout.</p>
    <div class="service-more"><svg width="20" height="10" viewBox="0 0 20 10"><path d="M0 5h18M14 1l4 4-4 4" fill="none" stroke="#888"/></svg>READ MORE</div>
  </section>

  <section class="abs service" style="left:403px">
    <div class="service-head">
      <svg width="58" height="30" viewBox="0 0 58 30"><path d="M2 8l10-5 8 4 8-3 10 3 8-4 10 5v8l-8 4-14 9-6-3-8-6-8-4H2z" fill="none" stroke="var(--navy)" stroke-width="2"/><path d="M20 14l8-4 10 8" fill="none" stroke="var(--navy)" stroke-width="2"/></svg>
      <span>Business Law and<br>Dispute Resolution</span>
    </div>
    <p class="service-body">It is a long established fact that a reader will be distractedlooking at its layout. It is a long established fact that a reader will be distracted-looking at its layout.</p>
    <div class="service-more"><svg width="20" height="10" viewBox="0 0 20 10"><path d="M0 5h18M14 1l4 4-4 4" fill="none" stroke="#888"/></svg>READ MORE</div>
  </section>

  <section class="abs service" style="left:682px">
    <div class="service-head">
      <svg width="52" height="36" viewBox="0 0 52 36"><circle cx="22" cy="19" r="15" fill="var(--navy)"/><path d="M8 16h28M10 25h24M22 4v30" stroke="#fff" stroke-width="1.2"/><path d="M30 10l18-8-6 10 8 2-4 3-8-2-6 6z" fill="var(--navy)" stroke="#fff" stroke-width="1"/></svg>
      <span>Migration Assistance</span>
    </div>
    <p class="service-body">It is a long established fact that a reader will be distractedlooking at its layout. It is a long established fact that a reader will be distracted-looking at its layout.</p>
    <div class="service-more"><svg width="20" height="10" viewBox="0 0 20 10"><path d="M0 5h18M14 1l4 4-4 4" fill="none" stroke="#888"/></svg>READ MORE</div>
  </section>

  <div class="abs stats-photo" role="img" aria-label="City skyline with a marina of moored yachts, tinted blue"></div>
  <svg class="abs hours-panel" width="1021" height="327" viewBox="0 0 1021 327">
    <polygon points="550,0 1021,0 1021,327 550,327 505,327 550,163 505,0" fill="var(--navy)"/>
  </svg>

  <div class="abs stat" style="left:102px"><div class="stat-num">13244</div><div class="stat-label">Happy Clients</div></div>
  <div class="abs stat" style="left:282px"><div class="stat-num">444</div><div class="stat-label">Awards Received</div></div>

  <div class="abs hours">
    <h2>Working Hours:</h2>
    <p>Lorem Ipsum is simply dummy text of the printing and typesetting industry.</p>
    <dl>
      <div><dt>Mon–Sat:</dt><dd>8:00 a.m – 11:00 p.m</dd></div>
      <div><dt>Sunday:</dt><dd>10:00 a.m – 12:00 p.m</dd></div>
    </dl>
  </div>

  <div class="abs principal"></div>
  <div class="abs portrait" role="img" aria-label="Black and white portrait of the firm's principal in a suit"></div>
  <div class="abs principal-name">Marcus Westbrook</div>
  <div class="abs principal-role">Principal at Westbrook Legal</div>
  <div class="abs principal-text">
    <p>Marcus's rare regulatory experience in public fundraisings and mergers and acquisitions is a compelling advantage for any company seeking to complete a significant transaction quickly.</p>
    <p>Marcus assisted draft the Securities Commission's regulatory guidance on prospectuses. With his team Marcus was awarded a National Service Achievement Medallion, “reserved for the highest level of recognition”, and awarded “to recognise the significant contribution made to the nation by individuals in the public service”.</p>
  </div>

  <h2 class="abs testi-title">Testimonials</h2>
  <div class="abs testi-sub"><i></i>What our client says<i></i></div>
  <div class="abs testi-name">Elena Morris</div>
  <p class="abs testi-quote">Lorem Ipsum is simply dummy text of the printing and typesetting industry. Lorem Ipsum has been the industry's standard dummy text ever since the 1500s, when an unknown printer took a galley of type and scrambled it to make a type specimen book.</p>
  <div class="abs arrows">
    <span><svg width="8" height="8" viewBox="0 0 8 8"><path d="M5 1L2 4l3 3" fill="none" stroke="#333" stroke-width="1.3"/></svg></span>
    <span><svg width="8" height="8" viewBox="0 0 8 8"><path d="M3 1l3 3-3 3" fill="none" stroke="#333" stroke-width="1.3"/></svg></span>
  </div>

  <div class="abs cta">
    <h3 class="abs">We are always ready to help you.</h3>
    <p class="abs">Lorem Ipsum is simply dummy text of the printing and typesetting industry.</p>
    <div class="abs btn">Hire Us</div>
  </div>

  <div class="abs footer">
    <h4 class="abs news-title">Subscribe Newsletter</h4>
    <div class="abs news-form"><span>Enter your email address...</span><b>SUBSCRIBE</b></div>
    <nav class="abs footer-nav"><span>Home</span><span>About Us</span><span>Services</span><span>News</span><span>Contact Us</span></nav>
    <div class="abs footer-divider"></div>
    <h4 class="abs follow-title">Follow Us</h4>
    <div class="abs follow-links"><span></span><span></span><span></span></div>
  </div>
  <div class="abs copyright">© 2017 Westbrook Legal All Rights Reserved</div>

</div>
</body>
</html>
```